New Business Cards for Torvin Group

We need a new Business Card to compliment our new logo. We are a vibrant design, manufacture and install business providing recreation areas, public parks and Municipal spaces. We want business cards that are classy, modern and clean.

We have recently changed our logo, and are celebrating our 40th anniversary. We want business cards with a new modern design to reflect our status.

Target Market(s)

Customers

Contact Information for Business Card

We need all the details of our 3 offices as per the business card attached. Please disregard the old logo on the business card, the other three files show our new logo.

Requirements
Must have
• All info as per attached business card but with new logo.
Nice to have

```html
<!DOCTYPE html>
<html lang="en">
<head>
<meta charset="utf-8">
<title>Torvin Group Business Card</title>
<link href="https://fonts.googleapis.com/css2?family=Barlow:wght@400;600&family=Montserrat:wght@600;700&family=Open+Sans:wght@400&display=swap" rel="stylesheet">
<style>
  :root {
    --backdrop: #a2a2a2;
    --brand-red: #ec3237;
    --brand-red-deep: #b8191f;
    --charcoal: #4a4a4d;
    --ink: #111111;
    --paper: #ffffff;
  }
  * { margin: 0; padding: 0; box-sizing: border-box; }
  html, body { width: 1200px; height: 1200px; overflow: hidden; background: var(--backdrop); }
  .canvas { position: relative; width: 1200px; height: 1200px; }

  .card { position: absolute; left: 296px; width: 608px; height: 348px; overflow: hidden; }
  .card-front { top: 252px; background: var(--paper); }
  .card-back { top: 701px; background: var(--brand-red); }

  /* front left */
  .brand-mark { position: absolute; left: 46px; top: 50px; width: 270px; display: flex; align-items: center; gap: 14px; }
  .brand-dot { flex: none; width: 44px; height: 44px; border-radius: 50%; background: var(--brand-red); }
  .brand-name { font-family: "Montserrat", sans-serif; font-weight: 700; font-size: 32px; line-height: 34px; letter-spacing: 0.5px; color: var(--charcoal); white-space: nowrap; }
  .brand-name span { display: block; }

  .holder { position: absolute; left: 0; width: 331px; top: 220px; text-align: center; }
  .holder-name { font-family: "Montserrat", sans-serif; font-weight: 700; font-size: 22px; letter-spacing: 0.6px; color: var(--ink); display: inline-block; padding: 0 1px 3px; border-bottom: 1px solid var(--ink); }
  .holder-title { font-family: "Montserrat", sans-serif; font-weight: 600; font-size: 11.5px; letter-spacing: 0.4px; color: var(--ink); margin-top: 5px; }

  .holder-contact { position: absolute; left: 86px; top: 283px; font-family: "Open Sans", sans-serif; font-size: 13.5px; color: var(--ink); line-height: 21px; }
  .holder-contact li { list-style: none; display: flex; align-items: center; gap: 6px; white-space: nowrap; }
  .holder-contact svg { width: 12px; height: 12px; fill: var(--brand-red); }

  .divider { position: absolute; left: 331px; top: 0; width: 10px; height: 100%; background: var(--charcoal); }
  .offices { position: absolute; left: 341px; top: 0; width: 267px; height: 100%; background: var(--brand-red); color: var(--paper); font-family: "Barlow", sans-serif; font-size: 12px; }
  .office { position: absolute; left: 48px; }
  .office h3 { font-weight: 400; font-size: 12px; line-height: 17.6px; margin-bottom: 2px; }
  .office li { list-style: none; display: flex; align-items: center; line-height: 17.6px; letter-spacing: 0.2px; white-space: nowrap; }
  .office svg { width: 10px; height: 10px; fill: var(--paper); margin-right: 5px; }
  .office-head { top: 20px; }
  .office-dubai { top: 121px; }
  .office-qatar { top: 219px; }
  .offices-web { position: absolute; left: 46px; bottom: 8px; font-weight: 600; font-size: 12.5px; letter-spacing: 0.3px; }

  /* back */
  .back-brand { position: absolute; left: 0; right: 0; top: 138px; display: flex; justify-content: center; align-items: center; gap: 16px; }
  .back-brand .brand-dot { width: 60px; height: 60px; background: var(--brand-red-deep); }
  .back-brand .brand-name { font-size: 50px; line-height: 60px; color: var(--brand-red-deep); }
  .back-web { position: absolute; left: 0; right: 0; bottom: 6px; text-align: center; font-family: "Open Sans", sans-serif; font-size: 17.5px; letter-spacing: 0.6px; color: var(--paper); }
</style>
</head>
<body>
<svg width="0" height="0" style="position:absolute">
  <defs>
    <symbol id="icon-pin" viewBox="0 0 10 10"><rect x="1" y="1" width="8" height="4"/><rect x="4" y="4" width="2" height="6"/></symbol>
    <symbol id="icon-phone" viewBox="0 0 10 10"><path d="M0 3 Q5 0 10 3 L10 4.5 L7.5 4.5 L7 3.5 L3 3.5 L2.5 4.5 L0 4.5Z"/><rect x="1.5" y="5" width="7" height="4"/></symbol>
    <symbol id="icon-fax" viewBox="0 0 10 10"><rect x="0" y="4" width="10" height="6"/><rect x="2" y="0" width="6" height="5"/></symbol>
    <symbol id="icon-mail" viewBox="0 0 10 10"><path d="M0 2 H10 V8 H0Z"/><path d="M0 2 L5 5.5 L10 2" fill="none" stroke="rgba(0,0,0,0.35)" stroke-width="0.8"/></symbol>
    <symbol id="icon-mobile" viewBox="0 0 10 12"><path d="M2 0 H8 A1 1 0 0 1 9 1 V11 A1 1 0 0 1 8 12 H2 A1 1 0 0 1 1 11 V1 A1 1 0 0 1 2 0Z M2.3 1.5 V9.5 H7.7 V1.5Z"/></symbol>
  </defs>
</svg>

<main class="canvas">
  <section class="card card-front">
    <div class="brand-mark">
      <span class="brand-dot"></span>
      <span class="brand-name"><span>TORVIN</span><span>GROUP</span></span>
    </div>

    <div class="holder">
      <div class="holder-name">SAMIR HADDAD</div>
      <div class="holder-title">MANAGING PARTNER</div>
    </div>
    <ul class="holder-contact">
      <li><svg viewBox="0 0 10 12"><use href="#icon-mobile"/></svg>: &nbsp;+971 (0)50 384 7162</li>
      <li><svg viewBox="0 0 10 10"><use href="#icon-mail"/></svg>: samir@torvingroup.com</li>
    </ul>

    <div class="divider"></div>

    <div class="offices">
      <div class="office office-head">
        <h3>Head Office</h3>
        <ul>
          <li><svg viewBox="0 0 10 10"><use href="#icon-pin"/></svg>: 41820 Abu Dhabi, U.A.E</li>
          <li><svg viewBox="0 0 10 10"><use href="#icon-phone"/></svg>: +971 (0)2 5830417</li>
          <li><svg viewBox="0 0 10 10"><use href="#icon-fax"/></svg>: +971 (0)2 5830418</li>
          <li><svg viewBox="0 0 10 10"><use href="#icon-mail"/></svg>: sales@torvingroup.com</li>
        </ul>
      </div>
      <div class="office office-dubai">
        <h3>Dubai Office</h3>
        <ul>
          <li><svg viewBox="0 0 10 10"><use href="#icon-pin"/></svg>: 517264 Dubai, U.A.E</li>
          <li><svg viewBox="0 0 10 10"><use href="#icon-phone"/></svg>: +971 (0)4 3762045</li>
          <li><svg viewBox="0 0 10 10"><use href="#icon-fax"/></svg>: +971 (0)4 3762098</li>
          <li><svg viewBox="0 0 10 10"><use href="#icon-mail"/></svg>: sales@torvingroup.com</li>
        </ul>
      </div>
      <div class="office office-qatar">
        <h3>Qatar Office</h3>
        <ul>
          <li><svg viewBox="0 0 10 10"><use href="#icon-pin"/></svg>: 20937 Doha, Qatar</li>
          <li><svg viewBox="0 0 10 10"><use href="#icon-phone"/></svg>: +974 44718302</li>
          <li><svg viewBox="0 0 10 10"><use href="#icon-fax"/></svg>: +974 44953617</li>
          <li><svg viewBox="0 0 10 10"><use href="#icon-mail"/></svg>: sales@torvingroup.com</li>
        </ul>
      </div>
      <div class="offices-web">www.torvingroup.com</div>
    </div>
  </section>

  <section class="card card-back">
    <div class="back-brand">
      <span class="brand-dot"></span>
      <span class="brand-name">TORVIN GROUP</span>
    </div>
    <div class="back-web">www.torvingroup.com</div>
  </section>
</main>
</body>
</html>
```